Occupational Therapist does home accessibility for disabled folks; needs business card design

We need a business card for a company in Portland, Oregon that specializes in making homes accessible, comfortable, and functional for people who are disabled or aging who would like to stay in THEIR home. Our medical background as Occupational Therapists allows us to translate the functional needs of the person into the recommendations for the design of the home remodel.

Target Market(s)

Elderly, children of elderly
People with disabilities, families of people with disabilities

Industry/Entity Type

Business

Contact Information for Business Card

Company name: HomeWise
Name: Danielle Reyes Crawford, OTR/L, CAPS, ECHM
Occupational Therapist, Home Modification & Accessibility Specialist
website: www.homewiseforyears.com
email: homewiseforyears@nestmail.example
phone: (503)218-4057
CCB #: 487315

Font styles to use
Sans Serif

Requirements
Must have
• My logo
• Easy to read font with contrasting background
• Please list the Services offered: Occupational Therapy, Home safety & accessibility assessments, Home modification consulting, project management
Nice to have
• Friendly, welcoming feel
Should not have
• Dark colored background

```html
<!DOCTYPE html>
<html lang="en">
<head>
<meta charset="utf-8">
<title>HomeWise Business Card</title>
<link href="https://fonts.googleapis.com/css2?family=Arimo:wght@400;700&display=swap" rel="stylesheet">
<style>
  :root {
    --gold: #e0a91c;
    --gold-deep: #c88e12;
    --grey: #8a8a8a;
    --grey-dark: #555555;
    --text: #3c3c3c;
    --card: #f7f7f7;
    --page: #e9e6e1;
  }
  * { margin: 0; padding: 0; box-sizing: border-box; }
  html, body {
    width: 1200px; height: 1023px; overflow: hidden;
    background: var(--page);
    font-family: "Arimo", Arial, sans-serif;
  }
  .sheet {
    position: relative; width: 1200px; height: 1023px;
  }
  .card {
    position: absolute; left: 290px; width: 620px; height: 354px;
    background: linear-gradient(160deg, #ffffff 0%, var(--card) 60%, #ececec 100%);
    border-radius: 18px;
    box-shadow: 0 10px 28px rgba(0,0,0,0.18);
    overflow: hidden;
  }
  .card--front { top: 110px; }
  .card--back { top: 560px; }

  /* Front */
  .front-brand {
    position: absolute; left: 0; right: 0; top: 0; bottom: 52px;
    display: flex; align-items: center; justify-content: center; gap: 18px;
  }
  .brand-square {
    width: 44px; height: 44px; background: var(--gold);
  }
  .brand-name {
    font-size: 72px; font-weight: 700; color: var(--gold);
    letter-spacing: -1px;
  }
  .front-band {
    position: absolute; left: 0; right: 0; bottom: 0; height: 52px;
    background: linear-gradient(90deg, var(--gold) 0%, var(--gold-deep) 100%);
    display: flex; align-items: center; justify-content: space-between;
    padding: 0 34px; color: #fff; font-size: 18px;
  }

  /* Back */
  .corner-tab {
    position: absolute; left: 0; top: 0;
  }
  .holder {
    position: absolute; left: 92px; top: 26px;
  }
  .holder-name {
    font-size: 27px; color: var(--gold); font-weight: 400;
  }
  .holder-role {
    margin-top: 6px; font-size: 14px; color: var(--grey-dark);
  }
  .contact-list {
    position: absolute; left: 40px; top: 130px; list-style: none;
  }
  .contact-item {
    display: flex; align-items: center; gap: 12px;
    font-size: 15px; color: var(--text); margin-bottom: 8px;
  }
  .contact-item svg { width: 15px; height: 15px; flex: none; }
  .services {
    position: absolute; left: 40px; top: 238px;
  }
  .services-title {
    font-size: 20px; color: var(--gold); margin-bottom: 8px;
  }
  .services-line {
    font-size: 14px; color: var(--text); margin-bottom: 5px;
  }
  .bullet { color: var(--gold); margin: 0 5px; }
  .bullet:first-child { margin-left: 0; }
  .back-brand {
    position: absolute; right: 34px; bottom: 28px;
    display: flex; align-items: center; gap: 8px;
  }
  .back-brand .brand-square { width: 16px; height: 16px; }
  .back-brand .brand-name { font-size: 24px; letter-spacing: 0; }
</style>
</head>
<body>
<main class="sheet">

  <section class="card card--front" aria-label="Card front">
    <div class="front-brand">
      <span class="brand-square"></span>
      <span class="brand-name">HomeWise</span>
    </div>
    <div class="front-band">
      <span class="front-web">www.homewiseforyears.com</span>
      <span class="front-ccb">CCB #: 487315</span>
    </div>
  </section>

  <section class="card card--back" aria-label="Card back">
    <svg class="corner-tab" width="84" height="44" viewBox="0 0 84 44">
      <polygon points="0,0 84,0 60,24 0,24" fill="var(--gold)"/>
      <polygon points="0,0 60,0 40,38 0,38" fill="#8c8c8c"/>
    </svg>

    <div class="holder">
      <h1 class="holder-name">Danielle Reyes Crawford, OTR/L, CAPS, ECHM</h1>
      <p class="holder-role">Home Modification &amp; Accessibility Specialist, Occupational Therapist</p>
    </div>

    <ul class="contact-list">
      <li class="contact-item">
        <svg viewBox="0 0 16 16"><circle cx="8" cy="8" r="7" fill="none" stroke="var(--gold)" stroke-width="1.4"/><path d="M5.6 4.6c.4-.3.8-.2 1 .2l.6 1.2c.1.3 0 .6-.2.8l-.4.4c.4.9 1.1 1.6 2 2l.4-.4c.2-.2.5-.3.8-.2l1.2.6c.4.2.5.6.2 1-.6.8-1.6 1-2.5.5-1.8-.9-3-2.1-3.8-3.8-.4-.9-.2-1.8.7-2.3z" fill="var(--gold)"/></svg>
        <span>(503)218-4057</span>
      </li>
      <li class="contact-item">
        <svg viewBox="0 0 16 16"><rect x="1.5" y="3.5" width="13" height="9" fill="none" stroke="var(--gold)" stroke-width="1.4"/><path d="M1.5 3.5 8 9l6.5-5.5" fill="none" stroke="var(--gold)" stroke-width="1.4"/></svg>
        <span>homewiseforyears@nestmail.example</span>
      </li>
      <li class="contact-item">
        <svg viewBox="0 0 16 16"><circle cx="8" cy="8" r="6.5" fill="none" stroke="var(--gold)" stroke-width="1.4"/><ellipse cx="8" cy="8" rx="3" ry="6.5" fill="none" stroke="var(--gold)" stroke-width="1.2"/><path d="M1.5 8h13M2.6 4.5h10.8M2.6 11.5h10.8" stroke="var(--gold)" stroke-width="1.1"/></svg>
        <span>www.homewiseforyears.com</span>
      </li>
    </ul>

    <div class="services">
      <h2 class="services-title">Our Services</h2>
      <p class="services-line"><span class="bullet">●</span>Occupational Therapy<span class="bullet">●</span>Home safety &amp; accessibility assessments</p>
      <p class="services-line">Project management<span class="bullet">●</span>Home modification consulting</p>
    </div>

    <div class="back-brand">
      <span class="brand-square"></span>
      <span class="brand-name">HomeWise</span>
    </div>
  </section>

</main>
</body>
</html>
```